Cedar Row Maintenance and Concierge Flyer

We need a flyer for cedar row maintenance and concierge service. We specialize in and provide residential maintenance and errand services to retired and semi retired persons living in the Lake Norman area. The services we include:
Lighting and plumbing repairs
Ceiling fan installation
Handicap accessories
Locks and security
Picture hanging
Hang blinds
Furniture arrangement / assembly
Pressure washing
Battery Jump start
and more...

Our Concierge services include:
Errand running
Grocery shopping
Wellness Checks
Dog Walk
Garbage Collection
and more...

We offer monthly service agreements and 24/7 access
Call text or e-mail for more information
704.555.0187
1cedarrowmaint@quillpostmail.com

The design should invoke a sense of trust and a customer service driven mission

Target Market(s)

Residential maintenance

Industry/Entity Type

Property Maintenance

Contact Information for Business Card

Derek Halvorsen
48176 Quimby Ferrel Rd.
Cornelius NC 28031
704.555.0187
with uploaded logo

Requirements
Nice to have
• Would like a postcard size flyer. Front and back
Should not have
• No pics of of people wearing hard hats or pics of blueprints. No pics of commercial or industrial maintenance.

```html
<!DOCTYPE html>
<html lang="en">
<head>
<meta charset="utf-8">
<title>Cedar Row Maintenance &amp; Concierge – Flyer</title>
<link rel="stylesheet" href="https://fonts.googleapis.com/css2?family=Questrial&family=Architects+Daughter&family=Montserrat:wght@700&display=swap">
<style>
  :root {
    --paper: #ffffff;
    --ink: #1e1e1e;
    --slate: #6d6e71;
    --accent: #d2232a;
  }
  * { margin: 0; padding: 0; box-sizing: border-box; }
  html, body { width: 800px; height: 1200px; overflow: hidden; background: var(--paper); }
  .flyer {
    position: relative;
    width: 800px;
    height: 1200px;
    background: var(--paper);
    font-family: "Questrial", "Century Gothic", sans-serif;
    color: var(--ink);
  }
  .brand {
    position: absolute;
    left: 60px;
    top: 70px;
    display: flex;
    align-items: center;
    gap: 28px;
  }
  .brand-dot {
    width: 100px;
    height: 100px;
    border-radius: 50%;
    background: var(--accent);
    flex: none;
  }
  .brand-name {
    color: var(--slate);
    font-weight: 400;
    line-height: 1;
  }
  .brand-name .primary { display: block; font-size: 74px; letter-spacing: 1px; }
  .brand-name .secondary { display: block; font-size: 27px; letter-spacing: 2px; margin-top: 16px; }
  .section-title {
    position: absolute;
    top: 280px;
    left: 0;
    width: 800px;
    text-align: center;
    font-family: "Architects Daughter", cursive;
    font-weight: 400;
    color: var(--accent);
    font-size: 38px;
  }
  .intro {
    position: absolute;
    top: 330px;
    left: 22px;
    width: 760px;
    font-size: 45px;
    line-height: 56px;
  }
  .offer {
    position: absolute;
    top: 618px;
    left: 22px;
    width: 340px;
    padding: 10px 0 12px 20px;
    border-left: 3px solid var(--accent);
    font-family: "Architects Daughter", cursive;
    color: var(--accent);
    font-size: 30px;
    line-height: 1.4;
  }
  .offer::before {
    content: "";
    position: absolute;
    top: 0;
    left: 0;
    width: 60px;
    border-top: 3px solid var(--accent);
  }
  .offer::after {
    content: "";
    position: absolute;
    bottom: 0;
    left: 0;
    width: 340px;
    border-bottom: 3px solid var(--accent);
  }
  .contact-prompt {
    position: absolute;
    top: 748px;
    right: 32px;
    text-align: right;
    font-size: 45px;
    line-height: 54px;
  }
  .contact-phone {
    position: absolute;
    top: 920px;
    right: 32px;
    font-family: "Montserrat", "Arial", sans-serif;
    font-weight: 700;
    font-size: 40px;
  }
  .contact-email {
    position: absolute;
    top: 1092px;
    left: 0;
    width: 800px;
    text-align: center;
    font-family: "Montserrat", "Arial", sans-serif;
    font-weight: 700;
    font-size: 33px;
  }
</style>
</head>
<body>
<div class="flyer">
  <header class="brand">
    <span class="brand-dot"></span>
    <span class="brand-name">
      <span class="primary">Cedar Row</span>
      <span class="secondary">MAINTENANCE &amp; CONCIERGE</span>
    </span>
  </header>

  <h2 class="section-title">Specialized Services</h2>

  <p class="intro">We specialize in and provide<br>residential maintenance and<br>errand services to retired and<br>semi retired persons living in<br>the Lake Norman area.</p>

  <p class="offer">We offer monthly<br>service agreements<br>and&nbsp; 24/7 access</p>

  <p class="contact-prompt">Call, text, or e-mail<br>for more information at:</p>

  <p class="contact-phone">704.555.0187</p>

  <p class="contact-email">1cedarrowmaint@quillpostmail.com</p>
</div>
</body>
</html>
```